Minimalist, Flat(Matte) design for a Beef Jerky packaging company. No bullshit company looking for a

Need a packaging design for a new Beef Jerky product(in English). The name of the company is 'Vellorn' and thus the packaging should reflect the bullish, tough, and simple nature of the beef jerky product. The finished product should communicate simplicity, minimalism, yet toughness and strength.

The logo should be simple, with a minimal number of colors , and should be either all white/cream, or have some red as well. Main colors should be white, cream, tinted red, and matte black. I think 4 colors max would be best. The closest example to an existing package style would be Kessip Noir clove cigarettes( image attached).

It will be on a matte black standing pouch package. See image for package type. Package dimensions:

Dimension: Width x Gusset x Height
INCH : 5.125" (W) x 3.125" (G) x 8.125" (H)
MILLIMETER : 130mm (W) x 80mm (G) x 205mm (H)

I don't have anything totally specific so artistic liberty is encouraged, provided the colors are kept to a minimum and looks consistent with the simple nature of the brand and the matte black packaging.

Also attached an existing beef jerky package with a similar style to what we're looking for.

Industry/Entity Type

It Company

Colors
f59195
ffffff

Requirements
Must have
• Low contrast, flat and minimalist design.
Should not have
• A complicated design with many colors. Gawdy/flashy design. Bright colors. High contrast.

```html
<!DOCTYPE html>
<html lang="en">
<head>
<meta charset="utf-8">
<title>Vellorn Package Design</title>
<link rel="stylesheet" href="https://fonts.googleapis.com/css2?family=Questrial&family=Oswald:wght@600&family=Open+Sans:ital,wght@0,400;0,700;1,800&display=swap">
<style>
:root{
  --matte-black:#221f20;
  --white:#ffffff;
  --tint-red:#f59195;
  --line:#8a8a8a;
  --ink:#555555;
}
*{margin:0;padding:0;box-sizing:border-box}
html,body{width:1200px;height:851px;overflow:hidden;background:var(--white)}
body{position:relative;font-family:"Open Sans",Arial,sans-serif;color:var(--ink)}
.sheet{position:absolute;left:26px;top:26px;width:1148px;height:798px;border:1px solid var(--line)}
.abs{position:absolute}
.option-badge{width:46px;height:46px;border:1.5px solid var(--line);border-radius:50%;
  display:flex;align-items:center;justify-content:center;font-family:"Questrial",sans-serif;font-size:22px;color:#888}
.panel{position:absolute;background:var(--matte-black);color:var(--white);text-align:center;height:214px;top:318px}
.panel.front{width:137px}
.panel.side{width:84px}
.panel > *{position:absolute;left:0;right:0}
.brand-thin{font-family:"Questrial",sans-serif;letter-spacing:0}
.brand-bold{font-family:"Oswald",sans-serif;font-weight:600}
.tagline{font-size:7px;line-height:9px}
.flavour-italic{font-weight:800;font-style:italic;font-size:14px;letter-spacing:1px}
.flavour-bold{font-family:"Oswald",sans-serif;font-weight:600;font-size:13px;letter-spacing:1.5px}
.net-weight{font-size:5px;line-height:6px;color:#ccc}
.dim-label{font-size:4.5px;color:#888}
.title-block{position:absolute;left:26px;top:703px;width:1148px;height:121px;border-top:1px solid var(--line)}
.title-block .row{position:absolute;left:0;right:0;border-top:1px solid var(--line)}
.sheet-title{position:absolute;left:0;right:0;top:6px;text-align:center;font-weight:700;font-size:16px;color:#666;letter-spacing:.5px}
.field{font-family:"Questrial",sans-serif;font-size:15px;color:#666}
.vline{position:absolute;width:1px;background:var(--line)}
.swatch{position:absolute;width:34px;height:25px;top:768px;border:1px solid #bbb}
.swatch-label{position:absolute;top:800px;font-size:5px;color:#999;text-align:center;width:60px}
</style>
</head>
<body>
<div class="sheet"></div>

<!-- option markers -->
<div class="abs option-badge" style="left:235px;top:177px">A</div>
<div class="abs option-badge" style="left:581px;top:177px">B</div>
<div class="abs option-badge" style="left:894px;top:177px">C</div>

<!-- dimension lines, option A -->
<svg class="abs" style="left:110px;top:266px" width="300" height="270" viewBox="0 0 300 270" aria-hidden="true">
  <g stroke="#9a9a9a" stroke-width=".6" fill="none">
    <line x1="48" y1="8" x2="185" y2="8"/><line x1="48" y1="4" x2="48" y2="50"/><line x1="185" y1="4" x2="185" y2="50"/>
    <line x1="203" y1="8" x2="287" y2="8"/><line x1="203" y1="4" x2="203" y2="50"/><line x1="287" y1="4" x2="287" y2="50"/>
    <line x1="10" y1="52" x2="10" y2="266"/><line x1="6" y1="52" x2="48" y2="52"/><line x1="6" y1="266" x2="48" y2="266"/>
  </g>
</svg>
<div class="abs dim-label" style="left:215px;top:267px">130 mm</div>
<div class="abs dim-label" style="left:347px;top:267px">80 mm</div>
<div class="abs dim-label" style="left:106px;top:420px;transform:rotate(-90deg);transform-origin:left top">205 mm</div>

<!-- option A -->
<div class="panel front" style="left:158px">
  <div class="brand-thin" style="top:44px;font-size:29px">VELLORN</div>
  <div class="tagline" style="top:101px">Hand crafted beef jerky</div>
  <div class="flavour-italic" style="top:124px">Peppered</div>
  <div class="net-weight" style="top:188px">NET WT.<br>5oz / 142g</div>
</div>
<div class="panel side" style="left:313px">
  <div class="brand-thin" style="top:97px;font-size:16px">VELLORN</div>
</div>

<!-- option B -->
<div class="panel front" style="left:480px">
  <div class="brand-bold" style="top:42px;font-size:22px">Vellorn</div>
  <div class="tagline" style="top:90px">Hand crafted<br>beef jerky</div>
  <div class="flavour-bold" style="top:122px">“PEPPERED”</div>
  <div class="net-weight" style="top:188px">NET WT.<br>5oz / 142g</div>
</div>
<div class="panel side" style="left:635px">
  <svg style="top:58px;left:27px" width="30" height="30" viewBox="0 0 30 30" aria-hidden="true"><circle cx="15" cy="15" r="14" fill="var(--tint-red)"/></svg>
  <div class="brand-bold" style="top:94px;font-size:14px">Vellorn</div>
  <div class="tagline" style="top:136px">Hand crafted<br>beef jerky</div>
</div>

<!-- option C -->
<div class="panel front" style="left:802px">
  <div class="brand-bold" style="top:48px;font-size:18px">VELLORN</div>
  <div class="tagline" style="top:90px">Hand crafted<br>beef jerky</div>
  <div class="flavour-bold" style="top:122px">“PEPPERED”</div>
  <div class="net-weight" style="top:188px">NET WT.<br>5oz / 142g</div>
</div>
<div class="panel side" style="left:956px">
  <div class="brand-bold" style="top:96px;font-size:14px;color:var(--tint-red)">VELLORN</div>
</div>

<!-- title block -->
<div class="title-block">
  <div class="sheet-title">VELLORN PACKAGE DESIGN</div>
  <div class="row" style="top:29px"></div>
  <div class="row" style="top:60px;left:250px;right:120px"></div>
  <div class="row" style="top:90px;left:250px;right:120px"></div>
  <div class="vline" style="left:250px;top:29px;height:92px"></div>
  <div class="vline" style="left:633px;top:29px;height:92px"></div>
  <div class="vline" style="left:1028px;top:29px;height:92px"></div>
  <div class="abs field" style="left:40px;top:38px">COLOR SWATCHES</div>
  <div class="abs field" style="left:264px;top:38px">DATE: 121115</div>
  <div class="abs field" style="left:264px;top:68px">SCALE: 1:1</div>
  <div class="abs field" style="left:264px;top:98px">UNITS AND DIMENSIONS: millimeter</div>
</div>
<div class="swatch" style="left:60px;background:var(--matte-black)"></div>
<div class="swatch" style="left:126px;background:var(--white)"></div>
<div class="swatch" style="left:191px;background:var(--tint-red);border-color:var(--tint-red)"></div>
<div class="swatch-label" style="left:47px">Matte black C</div>
<div class="swatch-label" style="left:113px">Cool white C</div>
<div class="swatch-label" style="left:178px">Tint red C</div>
</body>
</html>
```